'We're just a little bit different' business cards for an IT Startup

We are an Information Technology Start-up focusing on providing IT strategy services to large midcap and enterprise organisations. We need to create business cards which reflect us personally and our brand. Quorvix.io is looking to differentiate itself in the market by providing IT strategy that reflects Information technology today.
We would like business cards that:
- Are just a little bit different, so people read them
- Reflect that Quorvix.Io is a modern disruptive technology company
- Reinforces our brand – strategy reinvented
- Provides information about us that is deeper and richer than just here’s my mobile and email address. We’d like the business card to be a snapshot of who we individually. It might be fav movie, book, sports, favourite beer, my family etc, fav quote etc

I have attached a document which has details about me to use on a sample business card and it also includes snapshots of our website. Also attached is our logo. If you need more information please ask

Industry/Entity Type

Information Technology

Contact Information for Business Card

See attached document, for my personal details to use as a sample

Requirements
Must have
• my details
• web site - url quorvix.io
• something a little bit different
Nice to have
• I'd like to see the design incorporate information about us that lets them see us as fellow human beings not just a work person
Should not have
• standard bland business cards

```html
<!DOCTYPE html>
<html lang="en">
<head>
<meta charset="utf-8">
<title>Quorvix.io business cards</title>
<link rel="stylesheet" href="https://fonts.googleapis.com/css2?family=Open+Sans:wght@400;600;700&display=swap">
<style>
  :root {
    --brand-red: #ee1c25;
    --brand-red-soft: #d9303f;
    --brand-blue: #0f7fbd;
    --label-blue: #2f8fd8;
    --card-white: #ffffff;
    --backdrop: #e9e9ec;
  }
  * { margin: 0; padding: 0; box-sizing: border-box; }
  html, body { width: 1200px; height: 900px; overflow: hidden; }
  body {
    background: var(--backdrop);
    font-family: "Open Sans", Arial, sans-serif;
    position: relative;
  }
  .card {
    position: absolute;
    width: 560px;
    height: 320px;
    border-radius: 22px;
    overflow: hidden;
    box-shadow: 0 6px 18px rgba(0,0,0,0.18);
  }
  .card-shape { position: absolute; inset: 0; width: 100%; height: 100%; }

  /* Back card */
  .card--back { left: 60px; top: 100px; background: var(--brand-red); color: var(--card-white); }
  .back-wordmark {
    position: absolute; left: 0; right: 0; top: 58px;
    text-align: center;
  }
  .back-wordmark .name {
    font-size: 88px; font-weight: 700; letter-spacing: -2px; line-height: 1;
  }
  .back-wordmark .tagline {
    display: block; font-size: 15px; font-weight: 600; margin-top: 6px;
    letter-spacing: 4px; text-transform: uppercase; line-height: 1;
  }
  .about {
    position: absolute; left: 20px; right: 20px; top: 212px;
    text-align: center; font-size: 12.5px; line-height: 1.6;
  }
  .about .label { color: #bfe2ff; font-weight: 600; text-transform: uppercase; }

  /* Front card */
  .card--front { left: 580px; top: 480px; background: var(--card-white); }
  .front-wordmark {
    position: absolute; left: 352px; top: 78px; width: 180px;
    color: var(--card-white); text-align: center;
  }
  .front-wordmark .name { font-size: 42px; font-weight: 700; letter-spacing: -1px; line-height: 1; }
  .front-wordmark .tagline {
    display: block; font-size: 9.5px; font-weight: 600; margin-top: 5px;
    letter-spacing: 2.5px; text-transform: uppercase;
  }
  .person { position: absolute; left: 42px; top: 196px; }
  .person .full-name { color: var(--brand-blue); font-size: 22px; font-weight: 700; line-height: 1.1; }
  .person .role { color: var(--brand-red); font-size: 13px; font-weight: 600; margin-bottom: 8px; }
  .contact-list { list-style: none; }
  .contact-list li {
    display: flex; align-items: center; gap: 8px;
    color: var(--brand-blue); font-size: 14px; line-height: 1.45;
  }
  .contact-list svg { width: 11px; height: 11px; fill: var(--brand-red); flex: none; }
</style>
</head>
<body>

  <section class="card card--back" aria-label="Card back">
    <svg class="card-shape" viewBox="0 0 560 320" aria-hidden="true">
      <circle cx="290" cy="140" r="125" fill="var(--brand-red-soft)" opacity="0.8"/>
    </svg>
    <div class="back-wordmark">
      <div class="name">quorvix</div>
      <span class="tagline">strategy rebuilt</span>
    </div>
    <p class="about">
      <span class="label">Off the clock –</span> Trail cycling, kayaking, tennis, hiking, baking, chess, fixing radios<br>
      <span class="label">What drives me:</span> Good work should feel simple to the people it serves<br>
      Whatever we build, I want it to be useful, honest and well made
    </p>
  </section>

  <section class="card card--front" aria-label="Card front">
    <svg class="card-shape" viewBox="0 0 560 320" aria-hidden="true">
      <polygon points="300,0 560,0 560,215" fill="var(--brand-red)"/>
      <polygon points="0,250 18,250 42,320 0,320" fill="var(--brand-red)"/>
      <circle cx="442" cy="98" r="100" fill="var(--brand-blue)"/>
    </svg>
    <div class="front-wordmark">
      <div class="name">quorvix</div>
      <span class="tagline">strategy rebuilt</span>
    </div>
    <div class="person">
      <div class="full-name">Marcus Thale</div>
      <div class="role">Founder</div>
      <ul class="contact-list">
        <li>
          <svg viewBox="0 0 24 24" aria-hidden="true"><path d="M6.6 10.8a15.1 15.1 0 0 0 6.6 6.6l2.2-2.2c.3-.3.7-.4 1-.2 1.1.4 2.3.6 3.6.6.6 0 1 .4 1 1V20c0 .6-.4 1-1 1A17 17 0 0 1 3 4c0-.6.4-1 1-1h3.5c.6 0 1 .4 1 1 0 1.3.2 2.5.6 3.6.1.3 0 .7-.2 1z"/></svg>
          0400918273
        </li>
        <li>
          <svg viewBox="0 0 24 24" aria-hidden="true"><path d="M2 5h20v14H2zm2 2v.5l8 5 8-5V7zm0 2.8V17h16V9.8l-8 5z"/></svg>
          marcus@quorvix.io
        </li>
        <li>
          <svg viewBox="0 0 24 24" aria-hidden="true"><path d="M12 2a10 10 0 1 0 0 20 10 10 0 0 0 0-20zm6.9 6h-3a15 15 0 0 0-1.3-3.9A8 8 0 0 1 18.9 8zM12 4c.8 1.2 1.5 2.5 1.9 4h-3.8c.4-1.5 1.1-2.8 1.9-4zM4.3 14a8 8 0 0 1 0-4h3.4a16 16 0 0 0 0 4zm.8 2h3a15 15 0 0 0 1.3 3.9A8 8 0 0 1 5.1 16zm3-8h-3a8 8 0 0 1 4.3-3.9C8.8 5.3 8.4 6.6 8.1 8zM12 20c-.8-1.2-1.5-2.5-1.9-4h3.8c-.4 1.5-1.1 2.8-1.9 4zm2.3-6H9.7a14 14 0 0 1 0-4h4.6a14 14 0 0 1 0 4zm.3 5.9c.6-1.2 1-2.5 1.3-3.9h3a8 8 0 0 1-4.300 3.9zm1.7-5.9a16 16 0 0 0 0-4h3.4a8 8 0 0 1 0 4z"/></svg>
          www.quorvix.io
        </li>
      </ul>
    </div>
  </section>

</body>
</html>
```